Halcyon Reach needs a business card designed

We need a business card designed for Halcyon Reach, an expansion of K9 Systems Pty Ltd (www.k9systems.com.au)

We provide high quality professional services for the Australian space industry. Our clients include the Southern Launch Bureau and companies working in the space industry. We identify people with space related skills both locally and internationally who are then contracted by clients to create products and support space launch activities.

Colours to be used:
- Navy blue #000080
- Rocket metallic #8A7F8D
- Platinum #E5E4E2
- Black #000000
- White #FFFFFF

*Front of the card*
I have attached our Halcyon Reach logo, which needs to be the main item on the card. The 'Space' text should be placed to the right of the 'K9' part rather than below, similar to the attached K9 Systems card, which this card should match.

If subtext is included, however, it should read ‘Staffing • Advice • Delivery’ rather than the ‘Design • Build • Test • Maintain’ of the K9 Systems card.

A black background (rather than blue background in the K9 Systems card) might be good, with a white pattern as in the K9 Systems card. If colour is used, the logo should be in its standard colours (as provided for the Halcyon Reach logo).

*Back of the card*
Include a smaller Halcyon Reach logo on the back.

We need the following details for Halcyon Reach personnel (as a template for entry):
- Name
- Company Position
- Mobile Number
- Email
- Office Address
- Include the Halcyon Reach website: www.halcyonreach.com.au

Overall, we'd like to see a design that communicates the adventure of space, professional integrity, and customer service. We look forward to seeing what you can come up with.

Target Market(s)

We provide high quality professional services for the Australian space industry. Our clients include the Southern Launch Bureau and companies working in the space industry.

Contact Information for Business Card

- Name
- Company Position
- Mobile Number
- Email
- Office Address

Requirements
Must have
• See project description.

```html
<!DOCTYPE html>
<html lang="en">
<head>
<meta charset="utf-8">
<title>Halcyon Reach Business Card</title>
<link href="https://fonts.googleapis.com/css2?family=Open+Sans:wght@400;600;700&display=swap" rel="stylesheet">
<style>
  :root {
    --navy: #2b2a7c;
    --metal: #8a7f8d;
    --white: #ffffff;
    --stage: #2a2a2a;
    --text-grey: #8a8a8a;
  }
  * { box-sizing: border-box; margin: 0; padding: 0; }
  html, body { width: 1200px; height: 900px; overflow: hidden; }
  body {
    background: var(--stage);
    font-family: "Open Sans", Arial, sans-serif;
    position: relative;
  }
  .card {
    position: absolute;
    width: 620px;
    height: 354px;
    background: var(--white);
    overflow: hidden;
    box-shadow: 0 12px 30px rgba(0,0,0,0.45);
  }
  .card-back { left: 200px; top: 50px; }
  .card-front { left: 380px; top: 480px; }
  .card-art { position: absolute; inset: 0; width: 100%; height: 100%; }

  .brand { position: absolute; display: flex; align-items: center; }
  .brand-dot { border-radius: 50%; background: var(--navy); flex: none; }
  .brand-name { color: var(--navy); font-weight: 700; line-height: 1; white-space: nowrap; }
  .brand-tagline { position: absolute; color: var(--navy); font-weight: 600; white-space: nowrap; }

  .card-back .brand { left: 48px; top: 54px; gap: 10px; }
  .card-back .brand-dot { width: 22px; height: 22px; }
  .card-back .brand-name { font-size: 30px; }
  .card-back .brand-tagline { left: 80px; top: 94px; font-size: 10px; }

  .person { position: absolute; left: 90px; top: 160px; }
  .person-name { color: var(--navy); font-size: 20px; font-weight: 700; }
  .person-role { color: var(--text-grey); font-size: 14px; margin-top: 1px; }
  .person-address { color: var(--text-grey); font-size: 13px; line-height: 1.45; margin-top: 10px; }

  .contacts { position: absolute; left: 380px; top: 72px; list-style: none; font-size: 13px; color: var(--text-grey); line-height: 1.6; }
  .contacts b { color: var(--navy); font-weight: 700; margin-right: 4px; }

  .card-front .brand { left: 70px; top: 118px; gap: 14px; }
  .card-front .brand-dot { width: 38px; height: 38px; }
  .card-front .brand-name { font-size: 52px; }
  .card-front .brand-tagline { left: 122px; top: 186px; font-size: 15px; }
  .web-front { position: absolute; right: 26px; top: 316px; color: var(--white); font-size: 13px; font-weight: 600; }
</style>
</head>
<body>

<section class="card card-back" aria-label="Card back with contact details">
  <svg class="card-art" viewBox="0 0 620 354" aria-hidden="true">
    <path fill="var(--metal)" d="M0,354 L0,326 Q310,300 620,268 L620,354 Z"/>
    <path fill="var(--navy)" d="M0,354 L0,340 Q310,318 620,290 L620,354 Z"/>
  </svg>
  <div class="brand">
    <span class="brand-dot"></span>
    <span class="brand-name">Halcyon Reach</span>
  </div>
  <p class="brand-tagline">Staffing • Advice • Delivery</p>

  <div class="person">
    <p class="person-name">Morgan Ellery</p>
    <p class="person-role">President/CEO</p>
    <p class="person-address">0000 Harbour Rd. Unit 0000,<br>Adelaide, SA 0000</p>
  </div>

  <ul class="contacts">
    <li><b>p:</b>0412 555 018</li>
    <li><b>t:</b>08 5550 1190</li>
    <li><b>e:</b>morgan@halcyonreach.com.au</li>
    <li><b>w:</b>www.halcyonreach.com.au</li>
  </ul>
</section>

<section class="card card-front" aria-label="Card front with brand name">
  <svg class="card-art" viewBox="0 0 620 354" aria-hidden="true">
    <path fill="var(--metal)" d="M0,300 Q310,252 620,222 L620,354 L0,354 Z"/>
    <path fill="var(--navy)" d="M0,318 Q310,274 620,246 L620,354 L0,354 Z"/>
  </svg>
  <div class="brand">
    <span class="brand-dot"></span>
    <span class="brand-name">Halcyon Reach</span>
  </div>
  <p class="brand-tagline">Staffing • Advice • Delivery</p>
  <p class="web-front">www.halcyonreach.com.au</p>
</section>

</body>
</html>
```